Website Design for Business Law Firm

We have a logo and now we would like a web site design for our new website. Our small firm provides creative and aggressive transactional (not litigation) legal services to advise healthcare, technology, internet-based and traditional companies and investors in such companies on healthcare, technology, financing, mergers/acquisitions, real estate and other transactions, legal compliance and general corporate and business matters.

We would like to see a website design that is professional and appropriate for executives, professionals, investors and government regulators to visit, that conveys professionalism and competence while being a little edgy and modern - no typical legal motifs such as gavels, books, or scales of justice. We advise businesses and investors and guide them through complicated issues quickly, capably and differently from other law firms. We are part of the business team and get things done.

The logo is attached, and we like gray as a color to complement it. The intention of the logo is to convey that in a storm or challenging time, people come to this firm, and people come to this firm when they need the power and disruption to change things or shake them up.

I have also enclosed a picture of our business card for consideration.

On the other hand, you can check out the current simple site at www.venhollow.example to see we have used a space motif in the past to evoke that we help create stars (the nebula featured there). This is not a necessary part of the new website and it may look better without it.

We appreciate your creativity and look forward to designs.

Industry/Entity Type

Business

Requirements
Must have
• We anticipate the following pages, and you may submit different ideas for the different pages:
• 1. Landing page
• 2. Services pages - healthcare, IT/Technology, general counsel services, financings, mergers/acquisitions, mediation/arbitration, procurement and productization
• 3. About Us including contact information
• Our name and contact information:
• Quellane Law Firm, P.C.
• 8716 SW 19th Ave.
• Portland, OR 97213
• phone: 971.555.0143
• fax: 971.555.0187
Nice to have
• Please consider designs that enhance the impressions we are looking for
Should not have
• Please no gavels, scales of justice, law books, or similar traditional legal imagery.

```html
<!DOCTYPE html>
<html lang="en">
<head>
<meta charset="utf-8">
<title>Quellane Law Firm, P.C.</title>
<link href="https://fonts.googleapis.com/css2?family=Nanum+Gothic:wght@400;700&display=swap" rel="stylesheet">
<style>
:root{
  --sky-top:#1a1622;
  --sky-mid:#3a3450;
  --city-dark:#0c0c0e;
  --panel:rgba(52,52,54,.72);
  --logo-panel:#4a4a4a;
  --band:#616161;
  --white:#ffffff;
  --ink:#2a2a2a;
  --muted:#e6e6e6;
  --icon:#9aa0a8;
}
*{margin:0;padding:0;box-sizing:border-box}
html,body{width:1200px;height:1040px;overflow:hidden;background:var(--white)}
body{font-family:"Nanum Gothic",sans-serif;position:relative}
.hero-photo{position:absolute;left:0;top:0;width:1200px;height:850px;
  background:
    radial-gradient(ellipse at 50% 18%,rgba(120,110,160,.45),transparent 60%),
    linear-gradient(to bottom,var(--sky-top) 0%,var(--sky-mid) 32%,#25222c 48%,#141416 62%,var(--city-dark) 100%);}
.logo-panel{position:absolute;left:325px;top:70px;width:597px;height:176px;border-radius:16px;
  background:var(--logo-panel);display:flex;align-items:center;justify-content:center}
.logo-name{color:var(--white);font-size:62px;font-weight:400;letter-spacing:14px}
.services{position:absolute;left:144px;top:302px;width:928px;height:330px;border-radius:12px;background:var(--panel)}
.services h1{position:absolute;left:48px;top:26px;color:var(--white);font-size:30px;font-weight:700}
.service-list{list-style:none;position:absolute;top:83px;width:420px}
.service-list.left{left:54px}
.service-list.right{left:466px;width:450px}
.service-list li{color:var(--white);font-size:18.5px;height:28.1px;line-height:28px;padding-left:24px;position:relative;white-space:nowrap}
.service-list li::before{content:"";position:absolute;left:0;top:8px;width:13px;height:13px;border-radius:50%;
  background:radial-gradient(circle at 40% 35%,#fafafa,#b8b8b8 60%,#8a8a8a)}
.info-band{position:absolute;left:0;top:850px;width:1200px;height:92px;background:var(--band);text-align:center;color:var(--white)}
.info-band .address{font-size:20px;margin-top:22px}
.info-band .credit{font-size:12px;font-weight:700;margin-top:12px;color:var(--muted)}
.contact-bar{position:absolute;left:33px;top:963px;display:flex;align-items:center;gap:0;color:var(--ink);font-size:16px}
.contact-item{display:flex;align-items:center}
.contact-item svg{margin-right:8px}
.contact-item.email{margin-right:22px}
.contact-item.phone{margin-right:22px}
.copyright{position:absolute;left:34px;top:1003px;font-size:15px;color:var(--ink)}
.footer-name{position:absolute;left:860px;top:955px;width:309px;height:75px;display:flex;align-items:center;justify-content:center;
  color:#3c3c3c;font-size:34px;letter-spacing:6px}
</style>
</head>
<body>
<div class="hero-photo" role="img" aria-label="Night photograph of lightning striking over hills and a lit city below"></div>

<header class="logo-panel">
  <span class="logo-name">QUELLANE</span>
</header>

<section class="services">
  <h1>Pragmatic, Creative Services for Innovative Businesses</h1>
  <ul class="service-list left">
    <li>Strategic Alliances</li>
    <li>Business RElationships</li>
    <li>Outsourcing</li>
    <li>Procurements-Buying or Selling</li>
    <li>Licensing and Technology Exploitation</li>
    <li>Venture Formation and Startup</li>
    <li>Venture Financing</li>
    <li>Creative Private Financing Arrangements</li>
  </ul>
  <ul class="service-list right">
    <li>Mergers and Acquisitions</li>
    <li>Real Estate</li>
    <li>Contracts</li>
    <li>Audits, Analyses and Legal Project Management</li>
    <li>Local Counsel for Transactions and Due Diligence</li>
    <li>Vendor Management</li>
    <li>Dispute Resolution</li>
    <li>Service as a Mediator or Arbitrator</li>
  </ul>
</section>

<div class="info-band">
  <p class="address">Quellane Law Firm, P.C., P.O. Box 5120, Portland, OR 97213</p>
  <p class="credit">Image Credit : Stellar Archive, Orbital Survey Group, R.Tamsin (Deep Field Imaging Institute) and the Nebula Treasury Project Team</p>
</div>

<footer>
  <div class="contact-bar">
    <div class="contact-item email">
      <svg width="28" height="28" viewBox="0 0 28 28" aria-hidden="true">
        <rect x="1" y="3" width="26" height="22" rx="4" fill="#f2f2f2" stroke="#b5b5b5"/>
        <path d="M5 9 L14 16 L23 9" fill="none" stroke="#9a9a9a" stroke-width="1.5"/>
      </svg>
      <span>info@quellane.example</span>
    </div>
    <div class="contact-item phone">
      <svg width="46" height="30" viewBox="0 0 46 30" aria-hidden="true">
        <path d="M4 22 L10 10 H38 L44 22 Z" fill="#c9ced4" stroke="#8b929b"/>
        <rect x="4" y="22" width="40" height="5" rx="1" fill="#a9b0b8"/>
        <path d="M8 9 Q23 -1 38 9 L34 12 Q23 5 12 12 Z" fill="var(--icon)"/>
        <rect x="17" y="14" width="14" height="6" rx="1" fill="#eef0f2"/>
      </svg>
      <span>971.555.0143</span>
    </div>
    <div class="contact-item fax">
      <svg width="32" height="36" viewBox="0 0 32 36" aria-hidden="true">
        <rect x="8" y="1" width="16" height="14" fill="#fafafa" stroke="#b0b0b0"/>
        <rect x="2" y="12" width="28" height="20" rx="3" fill="#d6dadf" stroke="#8b929b"/>
        <rect x="6" y="17" width="12" height="4" fill="#f3f3f3"/>
        <circle cx="24" cy="19" r="1.6" fill="#c44"/>
        <rect x="6" y="25" width="20" height="3" fill="#aab1b9"/>
      </svg>
      <span>971.555.0172</span>
    </div>
  </div>
  <p class="copyright">Copyright © Quellane Law Firm. All rights reserved.</p>
  <div class="footer-name">QUELLANE</div>
</footer>
</body>
</html>
```